Simple and clean poster/flyer design needed for public speaker!

SIMPLE AND CLEAN DESIGN NEEDED FOR POSTER/FLYER

I AM a public speaker based in London (www.corvanlethby.com)
and I would like to have a custom-made flyer/poster
(preferably in adobe CS4 template format) that I con customize (just changing the text) for my various speeches, topics and locations

I am looking for something very simple and clean.
NO extravagance or crowded poster, but a rather beautiful clean and eye-catching design that clearly informs people what i am talking about, where and when.

Go to my website www.corvanlethby.com
to see the colour scheme and style that I like
my poster should be like the website, similar colours, logo, clean, simple and clear.

Summary

(1) simple and clean design
(2) design that fits my brand (see website)
(3) clear and eye-catching to promote my speeches
(4) customizable for my various talks, by simply chancing the text (Please Adobe Photoshop CS4 template format)
(5)in A3, A4, A5, A6 sizes, so i can use it for both flyers and small posters

ADDITIONS

BIG BOLD HEADLINE TO GRAP ATTENTION, greatest prominence

sub headline to explain, smaller than the headline, but still prominent on the poster

just a few bullet points to list the benefits and answer the “whats in for me”-question
this is for people who are already interested and continue reading, medium prominence.

WHERE, WHEN, HOW MUCH-information, in the lower section of the poster, little text, but clearly visible

only one point of CONTACT on my poster “www.corvanlethby.com”, bit big and clear so that it is very prominent

little text, effectively used
LESS IS MORE
Updates

contact me regarding logo files and any questions you may have!

for the logo files go to

https://share.dropvaultex.net/f/x.aspx?k=41c07d2e9ab35f18c6d2

click on the folder "logo pack" to see the files

thanks for your interest. hope to see great designs!
I am really looking forward to it
if you have any questions, please do not hesitate to ask

Kind Regards
Corvan
 

• Simple, clean design, text sparingly used.

• The mood should be light-hearted, calm, bright, simple and friendly, comic like

• a lot of white space, calling more attention to the content

• a light blue, dark blue, white and black colour scheme as seen on the homepage (www.corvanlethby.com) please use the exact same colours as seen on the homepage.

White being most predominant, 2 different blue used to highlight something, black for text on white background.

• One graphic would be cool, as long as it is blue. It could be waves-like graphic, or something like the white pattern in the background, in my case just in blue on white background > http://www.quillmereretreathouse.org/., I do not mean exactly this graphic and not that crowded but a simple single graphic in blue as long as it fits the theme and feel of my poster

Top o f the poster

• (a )One short bold headline (TALK TITLE) with a sub-headline below it (hook)

• or (b) headline as question (…....?) and below sub-headline offering the solution (my talk ;-) of course)

• 3 benefits as on homepage, that I can adapt for each talk (bottom right of my start site “what are you looking for?” either blue on white, or as in the page white on blue...whatever looks better and fits the design). Not sure how that looks, and if to include it!

• the bottom of the poster will have “Where”-information “when”-information “ticket price” info

• contact at the very bottom...for more into or to purchase tickets (my website and email)

If you have any questions or need clarification please write me!

Requirements
Must have
• lot of white space
• less is more - simple design
• little text, little graphics- only used when necessary to greatest effect.
• light, friendly, modern feel
• blue-color scheme

```html
<!DOCTYPE html>
<html lang="en">
<head>
<meta charset="utf-8">
<title>Living Without Strain – Poster</title>
<link rel="stylesheet" href="https://fonts.googleapis.com/css2?family=Archivo+Black&family=Open+Sans:wght@600;700&display=swap">
<style>
  :root {
    --stage: #e9eaec;
    --paper: #ffffff;
    --navy: #1b1f2b;
    --ink: #14161c;
    --slate: #767b84;
    --sky: #1aa3e0;
    --sky-soft: #6db5d6;
    --sky-pale: #cfe9f7;
  }
  * { box-sizing: border-box; margin: 0; padding: 0; }
  html, body { width: 1200px; height: 900px; overflow: hidden; background: var(--stage); }
  .poster {
    position: absolute; left: 310px; top: 40px; width: 580px; height: 820px;
    background: var(--paper); overflow: hidden;
    box-shadow: 0 6px 18px rgba(0,0,0,.18);
  }
  .headline {
    position: absolute; left: 38px; top: 34px;
    font: 72px/74px "Archivo Black", "Arial Black", sans-serif;
    color: var(--navy); letter-spacing: -1px;
  }
  .hero-figure {
    position: absolute; right: 14px; top: 6px; width: 210px; height: 210px;
    background: radial-gradient(circle, var(--sky) 0 12%, var(--sky-pale) 40%, rgba(255,255,255,0) 70%);
  }
  .ray-field {
    position: absolute; left: 0; right: 0; top: 255px; bottom: 0;
    background: radial-gradient(ellipse at 50% 55%, var(--paper) 0 18%, var(--sky-pale) 45%, var(--sky) 100%);
  }
  .hook-band {
    position: absolute; left: 24px; right: 24px; top: 270px; height: 42px;
    background: var(--navy); color: var(--paper);
    font: 700 22px/42px "Open Sans", Arial, sans-serif; text-align: center;
  }
  .benefit-panel {
    position: absolute; left: 0; right: 0; top: 330px; height: 300px;
    background: var(--paper);
    clip-path: polygon(0 90px, 100% 0, 100% 175px, 0 265px);
  }
  .benefits {
    position: absolute; left: 44px; top: 432px; width: 520px;
    transform: rotate(-12deg); transform-origin: left top;
    font: 27px/30px "Archivo Black", "Arial Black", sans-serif; color: var(--ink);
  }
  .benefits .question { color: var(--slate); }
  .benefits ul { list-style: none; }
  .details {
    position: absolute; right: 30px; top: 590px; width: 520px;
    transform: rotate(-4deg); text-align: right;
    font: 27px/31px "Archivo Black", "Arial Black", sans-serif; color: var(--slate);
  }
  .details .sep { color: var(--sky); }
  .contact { position: absolute; left: 52px; right: 30px; top: 706px; }
  .contact-label {
    background: var(--sky-soft); color: var(--paper); height: 36px; padding-left: 28px;
    font: 700 14px/36px "Open Sans", Arial, sans-serif; text-transform: uppercase;
  }
  .contact-url {
    background: var(--sky); color: var(--paper); height: 66px; padding-left: 24px;
    font: 700 37px/64px "Open Sans", Arial, sans-serif;
  }
</style>
</head>
<body>
  <main class="poster">
    <div class="ray-field" role="img" aria-label="Blue light rays bursting outward behind the content"></div>
    <h1 class="headline">Living<br>Without<br>Strain</h1>
    <div class="hero-figure" role="img" aria-label="Glowing blue figure with arms raised in joy"></div>
    <p class="hook-band">Free yourself from fear and worry... forever</p>
    <div class="benefit-panel"></div>
    <section class="benefits">
      <p class="question">WHAT ARE YOU LOOKING FOR?</p>
      <ul>
        <li>IMPROVED SELF-ESTEEM...</li>
        <li>INNER PEACE AND CALM...</li>
        <li>GREATER PURPOSE &amp;<br>MEANING IN LIFE...</li>
      </ul>
    </section>
    <section class="details">
      <p>24.09.10 <span class="sep">//</span> 09:00-16:00 <span class="sep">//</span></p>
      <p>WRENFOLD BARBICAN, LONDON <span class="sep">//</span></p>
      <p>TICKETS £12 <span class="sep">//</span></p>
    </section>
    <footer class="contact">
      <p class="contact-label">For more info and to buy tickets, visit:</p>
      <p class="contact-url">www.corvanlethby.com</p>
    </footer>
  </main>
</body>
</html>
```